Business Card for Veltrano, a french tech company

Tech company
New technologies
Serious design
Dark theme

User info :
Name: Mathis CORLAVE
Position: Co-Founder & CEO
Tel: (+33) 6 58 24 90 37
Email: mathis@veltrano.io
Website: www.veltrano.io
Address: 17 rue des Tanneurs 69002 LYON

Attached is the business logo file.

```html
<!DOCTYPE html>
<html lang="fr">
<head>
<meta charset="utf-8">
<title>Veltrano — Carte de visite</title>
<link href="https://fonts.googleapis.com/css2?family=Montserrat:wght@400;500;700;800&display=swap" rel="stylesheet">
<style>
  :root {
    --page-bg: #e4e5e8;
    --card-white: #ffffff;
    --card-white-end: #f4f4f5;
    --ink-navy: #0f3566;
    --ink-dark: #15163a;
    --ink-text: #1b1b24;
    --band-magenta: #ee0fb4;
    --band-purple: #a70be6;
    --night-start: #0e0a45;
    --night-mid: #161d5c;
    --night-end: #0a3a6e;
    --white: #ffffff;
  }
  * { box-sizing: border-box; margin: 0; padding: 0; }
  html, body { width: 1200px; height: 1200px; overflow: hidden; }
  body {
    background: var(--page-bg);
    font-family: "Montserrat", sans-serif;
    display: flex;
    flex-direction: column;
    align-items: center;
    justify-content: center;
    gap: 60px;
  }
  .card {
    width: 840px;
    height: 480px;
    border-radius: 34px;
    position: relative;
    overflow: hidden;
    box-shadow: 0 12px 30px rgba(0,0,0,.18);
  }
  /* Front */
  .card-front {
    background: linear-gradient(180deg, var(--card-white) 0%, var(--card-white-end) 100%);
  }
  .card-front .brand-mark {
    position: absolute;
    top: 110px;
    right: 110px;
    font-weight: 800;
    font-size: 64px;
    color: var(--ink-dark);
    letter-spacing: -1px;
  }
  .identity {
    position: absolute;
    left: 70px;
    top: 215px;
  }
  .identity .full-name {
    font-weight: 800;
    font-size: 30px;
    color: var(--ink-navy);
    letter-spacing: 0.5px;
    line-height: 1;
  }
  .identity .position {
    font-weight: 500;
    font-size: 16px;
    color: var(--ink-text);
    letter-spacing: 1px;
    margin-top: 4px;
  }
  .contact-list {
    list-style: none;
    margin-top: 22px;
  }
  .contact-list li {
    display: flex;
    align-items: flex-start;
    gap: 14px;
    font-size: 18px;
    font-weight: 500;
    color: var(--ink-text);
    line-height: 1.3;
    margin-bottom: 6px;
  }
  .contact-list svg {
    width: 20px;
    height: 20px;
    flex: none;
    margin-top: 2px;
    fill: var(--ink-dark);
  }
  .band {
    position: absolute;
    left: 0; right: 0; bottom: 0;
    height: 22px;
    background: linear-gradient(90deg, var(--band-magenta), var(--band-purple));
  }
  /* Back */
  .card-back {
    background: linear-gradient(100deg, var(--night-start) 0%, var(--night-mid) 50%, var(--night-end) 100%);
    display: flex;
    align-items: center;
    justify-content: center;
  }
  .card-back .wordmark {
    font-weight: 800;
    font-size: 86px;
    color: var(--white);
    letter-spacing: 2px;
    text-transform: uppercase;
  }
</style>
</head>
<body>
  <section class="card card-front" aria-label="Recto">
    <div class="brand-mark">Veltrano</div>
    <div class="identity">
      <h1 class="full-name">MATHIS CORLAVE</h1>
      <p class="position">CO-FOUNDER &amp; CEO</p>
      <ul class="contact-list">
        <li>
          <svg viewBox="0 0 24 24" aria-hidden="true"><path d="M6.6 10.8a15.1 15.1 0 0 0 6.6 6.6l2.2-2.2a1 1 0 0 1 1-.25 11.4 11.4 0 0 0 3.6.57 1 1 0 0 1 1 1V20a1 1 0 0 1-1 1A17 17 0 0 1 3 4a1 1 0 0 1 1-1h3.5a1 1 0 0 1 1 1c0 1.25.2 2.45.57 3.6a1 1 0 0 1-.25 1z"/></svg>
          (+33) 6 58 24 90 37
        </li>
        <li>
          <svg viewBox="0 0 24 24" aria-hidden="true"><path d="M2 5h20v14H2z M4 7v.4l8 5.2 8-5.2V7z" fill-rule="evenodd"/></svg>
          mathis@veltrano.io
        </li>
        <li>
          <svg viewBox="0 0 24 24" aria-hidden="true"><path d="M12 2a10 10 0 1 0 0 20 10 10 0 0 0 0-20zm6.9 6h-2.9a15.6 15.6 0 0 0-1.4-3.6A8 8 0 0 1 18.9 8zM12 4c.8 1.2 1.5 2.5 1.9 4h-3.8c.4-1.5 1.1-2.8 1.9-4zM4.3 14a8 8 0 0 1 0-4h3.4a16.5 16.5 0 0 0 0 4zm.8 2h2.9c.3 1.3.8 2.5 1.4 3.6A8 8 0 0 1 5.1 16zM8 8H5.1a8 8 0 0 1 4.3-3.6C8.8 5.5 8.3 6.7 8 8zm4 12c-.8-1.2-1.5-2.5-1.9-4h3.8c-.4 1.5-1.1 2.8-1.9 4zm2.3-6H9.7a14.7 14.7 0 0 1 0-4h4.6a14.7 14.7 0 0 1 0 4zm.3 5.6c.6-1.1 1.1-2.3 1.4-3.6h2.9a8 8 0 0 1-4.3 3.6zm1.7-5.6a16.5 16.5 0 0 0 0-4h3.4a8 8 0 0 1 0 4z"/></svg>
          www.veltrano.io
        </li>
        <li>
          <svg viewBox="0 0 24 24" aria-hidden="true"><path d="M12 2a7 7 0 0 0-7 7c0 5.2 7 13 7 13s7-7.8 7-13a7 7 0 0 0-7-7zm0 9.5A2.5 2.5 0 1 1 12 6.5a2.5 2.5 0 0 1 0 5z"/></svg>
          <span>17 rue des Tanneurs<br>69002 LYON</span>
        </li>
      </ul>
    </div>
    <div class="band"></div>
  </section>

  <section class="card card-back" aria-label="Verso">
    <div class="wordmark">Veltrano</div>
  </section>
</body>
</html>
```